IT COMPANYcutting edge tec business card

we are IT company that building any apps.
we need business card in japanese and english
You don’t have to include all information in front one you can attach part of that information to back-side
company name : 株式会社ひかりの丘 (BRIGHTHILL Inc.)
concept : cutting-edge technology
role : 取締役 (director)
name : 呉 炫秀 (Oh Hyeonsuk)
post number : 154-0038
address : 東京都世田谷区西若葉台5-14-8 (5-14-8, Nishiwakabadai, Setagaya Ku, Tokyo To, 154-0038, Japan)
Tel:+81-3-5917-2846
Mobile:+81-80-7253-3169
Email : hoh@brighthill-lab.com
website : www.brighthill-lab.com

we dont have logo so please make it as well
we also looking for designer who can make homapage design.

Contact Information for Business Card

cutting-edge design and modern for IT

Font styles to use
Sans Serif

Colors
34a6d7
33b8a4
6092c4
3377b5
886aae
6b449b
b868aa
a64599

Requirements
Must have
• Simple but designed

```html
<!DOCTYPE html>
<html lang="ja">
<head>
<meta charset="utf-8">
<title>BRIGHTHILL Inc. — Business Card</title>
<link rel="stylesheet" href="https://fonts.googleapis.com/css2?family=Montserrat:wght@400;500;600;700&family=Noto+Sans+JP:wght@400;500&display=swap">
<style>
  :root {
    --page-bg: #d9d9db;
    --card-bg: #1b1b1d;
    --card-edge: #2a2a2d;
    --accent: #34a6d7;
    --ink: #f2f2f2;
    --ink-soft: #d8d8d8;
  }
  * { box-sizing: border-box; margin: 0; padding: 0; }
  html, body {
    width: 1200px; height: 896px; overflow: hidden;
    background: var(--page-bg);
    font-family: "Montserrat", "Noto Sans JP", sans-serif;
  }
  .stage {
    width: 1200px; height: 896px;
    display: flex; align-items: center; justify-content: center; gap: 90px;
  }
  .card {
    position: relative;
    width: 340px; height: 560px;
    background: var(--card-bg);
    border-radius: 28px;
    box-shadow: 0 0 0 1px var(--card-edge), 0 18px 40px rgba(0,0,0,.25);
    overflow: hidden;
    color: var(--ink);
  }

  /* Back side: rotated lockup */
  .card-back .lockup {
    position: absolute; left: 50%; top: 50%;
    width: 460px;
    transform: translate(-50%, -50%) rotate(-90deg);
    text-align: left;
    padding-left: 40px;
  }
  .company-jp {
    font-family: "Noto Sans JP", sans-serif;
    font-weight: 400; color: var(--accent);
    letter-spacing: .04em;
  }
  .company-en { font-weight: 700; letter-spacing: .03em; line-height: 1.05; }
  .post { font-weight: 400; letter-spacing: .04em; }

  .card-back .company-jp { font-size: 27px; }
  .card-back .company-en { font-size: 33px; color: var(--accent); }
  .card-back .post { font-size: 20px; color: var(--ink); margin-top: 4px; }

  /* Front side */
  .card-front { padding: 46px 30px 0 30px; }
  .card-front .company-jp { font-size: 25px; }
  .card-front .company-en { font-size: 31px; color: var(--ink); margin-top: 2px; }
  .card-front .post { font-size: 19px; color: var(--ink); margin-top: 4px; }

  .person { margin-top: 58px; }
  .person-name {
    font-size: 22px; color: var(--accent); font-weight: 500;
    font-family: "Montserrat", "Noto Sans JP", sans-serif;
  }
  .person-role {
    font-family: "Noto Sans JP", "Montserrat", sans-serif;
    font-size: 14px; color: var(--ink-soft); margin-top: 2px;
  }

  .contacts { list-style: none; margin-top: 14px; }
  .contacts li {
    display: flex; align-items: center; gap: 8px;
    font-size: 15px; line-height: 22px; color: var(--ink); letter-spacing: .03em;
  }
  .contacts svg { width: 13px; height: 13px; flex: none; fill: none; stroke: var(--accent); stroke-width: 1.8; }

  .address {
    margin-top: 16px; font-style: normal;
    font-size: 15px; line-height: 22px; color: var(--ink); letter-spacing: .03em;
  }
  .address .jp { font-family: "Noto Sans JP", sans-serif; }
</style>
</head>
<body>
<main class="stage">
  <section class="card card-back" aria-label="Card back">
    <div class="lockup">
      <p class="company-jp">株式会社ひかりの丘</p>
      <p class="company-en">BRIGHTHILL Inc.</p>
      <p class="post">Post number: 154-0038</p>
    </div>
  </section>

  <section class="card card-front" aria-label="Card front">
    <header>
      <p class="company-jp">株式会社ひかりの丘</p>
      <p class="company-en">BRIGHTHILL Inc.</p>
      <p class="post">Post number : 154-0038</p>
    </header>

    <div class="person">
      <p class="person-name">呉 炫秀 (Oh Hyeonsuk)</p>
      <p class="person-role">取締役 (director)</p>
    </div>

    <ul class="contacts">
      <li>
        <svg viewBox="0 0 16 16"><path d="M4 1.5l2.2 3-1.4 1.6c.9 2 2.5 3.6 4.5 4.5l1.6-1.4 3 2.2-1.2 2.6C7.5 14 2 8.5 1.5 3.1z"/></svg>
        +81-80-7253-3169
      </li>
      <li>
        <svg viewBox="0 0 16 16"><path d="M2 6c3.5-3 8.5-3 12 0l-1.8 2-2-1V5.5c-1.4-.4-3-.4-4.4 0V7l-2 1z"/><rect x="4" y="9" width="8" height="5" rx="1"/></svg>
        +81-3-5917-2846
      </li>
      <li>
        <svg viewBox="0 0 16 16"><rect x="1.5" y="3.5" width="13" height="9" rx="1"/><path d="M1.5 4l6.5 5 6.5-5"/></svg>
        hoh@brighthill-lab.com
      </li>
      <li>
        <svg viewBox="0 0 16 16"><circle cx="8" cy="8" r="6.5"/><path d="M1.5 8h13M8 1.5c-3 3.5-3 9.5 0 13M8 1.5c3 3.5 3 9.5 0 13"/></svg>
        www.brighthill-lab.com
      </li>
    </ul>

    <address class="address">
      <span class="jp">東京都世田谷区西若葉台</span><br>
      (Nishiwakabadai, Setagaya<br>
      Ku, Tokyo To, 154-0038,Japan)
    </address>
  </section>
</main>
</body>
</html>
```